New Laundromat Promotion in local area postcode in Brisbane.

NEED DOUBLE SIDED DL SIZED FLYER DESIGN IN COLOUR.
New laundromat has opened for business and I need to draw local customers in to try it. The laundromat has a green environmentally friendly and funky new age theme with following features: live vertical plant wall, all furniture made from recycled timber pallets, arcade game machine with popular games like blipzor and comet raiders.
Laundromat has 6 double load washers, 1 giant quadruple load washer and 6 high speed dryers. All machines are newest technology energy efficient machines imported from USA.
Laundromat also has a vending machine for customers to purchase cheap drinks and chips at only a $1 each.
Opening special till 31 jan 2014 is:
Double load washers $2 instead of normal price $5
Giant quadruple load washer $5 instead of normal price $8
Dryers $2 for 25 mins instead of $3
Arcade games FREE play
Reason: Have posted a clarification re. Size of the flyer. Am looking for double sided DL sized flyer in colour.
Target Market(s)
Inner city neighbourhood with a 20-35 age demographic. Must appeal to young people and grab their attention. Would like something funky and high energy. Lots of colour maybe...
Industry/Entity Type
Games
Requirements
Must have
- "Conveniently located at the corner of Wallace and Birch Road in Ferren Point, right next to the BJG. Plenty of parking available."
Please also use the branding "FoamHaven - Laundromat with a difference"
Please Also insert a
Google Map showing laundromat location:
318 Birch Road (intersection with WALLACE road)
Ferren Point
NORTHVALE 4990
Nice to have
- Colour, attention grabbing. Anything but what you would expect a normal laundromat to be.
Should not have
- Do not position it as a traditional laundromat. Must come
across as different, modern, young and hip! Must grab attention and get people to drop in to see it.

```html
<!DOCTYPE html>
<html lang="en">
<head>
<meta charset="utf-8">
<title>FoamHaven – Laundromat with a difference – DL flyer</title>
<link rel="stylesheet" href="https://fonts.googleapis.com/css2?family=Oswald:wght@400;500;700&family=Patrick+Hand&display=swap">
<style>
  :root{
    --bg:#e9e9e9;
    --red:#d5232f;
    --orange:#e8452a;
    --teal:#1aa3b8;
    --teal-light:#8fd3dc;
    --teal-dark:#1d5f6c;
    --grey-band:#4a4a4a;
    --yellow:#f4e21a;
    --white:#ffffff;
    --pink:#e9a1a4;
  }
  *{box-sizing:border-box;margin:0;padding:0}
  html,body{width:1200px;height:1000px;overflow:hidden;background:var(--bg)}
  .canvas{position:relative;width:1200px;height:1000px}
  .panel{position:absolute;top:42px;width:414px;height:858px;overflow:hidden;
    background:linear-gradient(180deg,#4b3a2a 0%,#2d3b33 25%,#3a4a4c 45%,#2b3032 70%,#3b3d3e 100%)}
  .panel--front{left:173px}
  .panel--back{left:646px}
  .panel__photo{position:absolute;inset:0}
  .deco{position:absolute;border-radius:50%;background:rgba(40,170,160,.45)}
  .deco--a{left:-20px;top:100px;width:170px;height:170px}
  .deco--b{left:120px;top:170px;width:160px;height:160px;background:rgba(40,170,160,.35)}
  .deco--c{left:250px;top:40px;width:190px;height:190px;background:rgba(60,140,80,.3)}
  .basket{position:absolute;left:82px;top:258px;width:270px;height:270px;border-radius:50%;
    background:radial-gradient(circle at 50% 45%,#c6c3c8 0%,#9a6e6e 35%,#d33140 60%,#f2f2f2 78%);
    border:3px solid #fff}
  .tagline{position:absolute;left:72px;top:450px;width:262px;height:24px;background:var(--red);
    color:#fff;font:500 16px/24px "Oswald",sans-serif;letter-spacing:.5px;text-align:center}
  .brand{position:absolute;left:50px;top:474px;width:334px;height:48px;background:var(--white);
    text-align:center;color:var(--red);font:700 40px/48px "Oswald",sans-serif;letter-spacing:2px}
  .subline{position:absolute;left:72px;top:522px;width:298px;height:28px;background:var(--grey-band);
    color:#fff;font:400 21px/28px "Patrick Hand",sans-serif;text-align:center}
  .features{position:absolute;left:48px;top:552px;width:342px;padding:7px 10px 8px;background:var(--teal)}
  .features__text{color:#fff;font:400 11.5px/14px "Oswald",sans-serif;text-transform:uppercase}
  .features__note{color:var(--yellow);font:400 15px/16px "Patrick Hand",sans-serif;margin-top:4px}
  .special{position:absolute;left:54px;top:654px;width:346px;padding:9px 12px;background:var(--orange);
    color:#fff;font:400 12px/16px "Oswald",sans-serif;text-transform:uppercase}
  .special__head{font:500 17px/20px "Oswald",sans-serif}
  .cta{position:absolute;left:90px;top:738px;width:172px;height:28px;background:var(--red);
    color:#fff;font:italic 500 16px/28px "Oswald",sans-serif;text-align:center}
  .phone-band{position:absolute;left:64px;top:768px;width:306px;height:48px;background:var(--teal-light);
    color:var(--teal-dark);font:500 38px/48px "Oswald",sans-serif;text-align:center;letter-spacing:1px}
  .foot-band{position:absolute;left:0;right:0;bottom:0;height:40px;background:var(--pink);opacity:.8}
  .map{position:absolute;left:31px;top:140px;width:380px;height:380px;border-radius:50%;border:6px solid #fff;
    background:linear-gradient(135deg,#9fc6e8 0%,#e9e5dc 30%,#f0ece3 60%,#f6d56b 75%,#e9e5dc 100%)}
  .address-block{position:absolute;left:0;right:0;top:533px;height:325px;background:var(--red);color:#fff;text-align:center}
  .address{padding-top:8px;font:400 26px/28px "Patrick Hand",sans-serif}
  .rule{width:345px;height:3px;background:#fff;margin:16px auto 14px}
  .directions{font:500 18px/25px "Oswald",sans-serif;text-transform:uppercase}
</style>
</head>
<body>
<div class="canvas">

  <section class="panel panel--front">
    <div class="panel__photo" role="img" aria-label="Photo of the laundromat interior with washers, plant wall and tiled floor"></div>
    <div class="deco deco--a"></div>
    <div class="deco deco--b"></div>
    <div class="deco deco--c"></div>
    <div class="basket" role="img" aria-label="Photo of a red laundry basket full of clothes"></div>
    <div class="tagline">YOUR CLOTHING OUR CARE!!</div>
    <h1 class="brand">FOAMHAVEN</h1>
    <p class="subline">Laundromat with a difference</p>
    <div class="features">
      <p class="features__text">Laundromat has 6 double load washers, 1 giant quadruple load washer and 6 high speed dryers. All machines are newest technology energy efficient machines imported from USA.</p>
      <p class="features__note">Laundromat also has a vending machine for customers to purchase cheap drinks and chips at only a $1 each</p>
    </div>
    <div class="special">
      <p class="special__head">Opening special till 31 Jan 2014 is:</p>
      <p>Double load washers $2 instead of normal price $5</p>
      <p>Giant quadruple load washer $5 instead of normal price $8</p>
      <p>Dryers $2 for 25 mins instead of $3 arcade games free play</p>
    </div>
    <div class="cta">CALL US FOR MORE INFO</div>
    <div class="phone-band">0400 555 019</div>
    <div class="foot-band"></div>
  </section>

  <section class="panel panel--back">
    <div class="panel__photo" role="img" aria-label="Photo of the laundromat interior with washers and plant wall"></div>
    <div class="deco deco--a"></div>
    <div class="deco deco--c"></div>
    <div class="map" role="img" aria-label="Street map of the neighbourhood with the laundromat location circled and marked Offer Here"></div>
    <div class="address-block">
      <p class="address">318 Birch Road<br>(intersection with WALLACE road)<br>Ferren Point NORTHVALE 4990</p>
      <div class="rule"></div>
      <p class="directions">Conveniently located at the corner of Wallace<br>and Birch Road in Ferren Point,<br>right next to the BJG.<br>Plenty of parking available</p>
    </div>
  </section>

</div>
</body>
</html>
```